Pomme Sauvage Riding School Flyer Design

We need a flyer for our Horse riding school, called Pomme Sauvage Riding School.

At Pomme Sauvage Riding School, Horses and ponies are carefully matched to suit each rider's experience, ability and confidence. I am a Qualified instructor, equipped to train all levels from nervous beginners to the more advanced.

Horse riding is fun! Riders, particularly children, are taught not only skills on the horse, but skills that are integral to good horsemanship and ownership of horses.

We regularly host Ladies Days, Guest Instructors, 1 hour Trail Rides and Pony Ride Days!

We teach people how to interact safely with, and care for horses so they develop a genuine love and respect for the animals and the sport.

In addition to fundamental riding techniques including walk, trot, and canter, we teach our students:
Grooming and Care of horses, Safety around horses, Balance and Co-Ordination, How to saddle up and care for Tack, Responsibility for equipment and horse, Confidence and Confidence Building for all Ages.

Private and group lessons start at 5 years of age upwards.

We recommend children 4 years and under partake in 15 minute pony rides, mainly due to their attention span!

```html
<!DOCTYPE html>
<html lang="en">
<head>
<meta charset="utf-8">
<title>Pomme Sauvage Riding School Flyer</title>
<link rel="stylesheet" href="https://fonts.googleapis.com/css2?family=Open+Sans:wght@400;700;800&family=Oswald:wght@400;500&display=swap">
<style>
  :root {
    --page: #e9e8e4;
    --paper: #ffffff;
    --slate: #4a4d47;
    --slate-text: #eef0ea;
    --sage: #b8bdb2;
    --sage-dark: #3f433c;
    --ink-green: #5a6055;
    --photo-light: #c9cbc6;
    --photo-dark: #55574f;
  }
  * { box-sizing: border-box; margin: 0; padding: 0; }
  html, body { width: 1200px; height: 1000px; overflow: hidden; }
  body {
    background: var(--page);
    font-family: "Open Sans", Arial, sans-serif;
    position: relative;
  }
  .flyer {
    position: absolute;
    left: 80px; top: 140px;
    width: 1040px; height: 720px;
    background: var(--paper);
    box-shadow: 0 10px 30px rgba(0,0,0,0.25);
    overflow: hidden;
  }
  .info-panel {
    position: absolute;
    left: 0; top: 0;
    width: 600px; height: 600px;
    background: var(--slate);
    color: var(--slate-text);
  }
  .intro { padding: 44px 36px 0 36px; }
  .intro-lead {
    font-weight: 800;
    font-size: 20.5px;
    line-height: 1.38;
  }
  .intro-body {
    margin-top: 12px;
    font-size: 14.5px;
    line-height: 1.42;
    color: #d7dad3;
  }
  .events-band {
    position: absolute;
    left: 0; top: 290px;
    width: 600px; height: 88px;
    background: var(--sage);
    clip-path: polygon(0 14%, 100% 0, 100% 82%, 0 100%);
    padding: 26px 36px 0 40px;
  }
  .events-text {
    font-weight: 800;
    font-size: 19px;
    line-height: 1.3;
    color: var(--sage-dark);
  }
  .teaching { position: absolute; left: 0; top: 394px; padding: 0 36px 0 40px; width: 600px; }
  .teaching-lead { font-size: 14.5px; line-height: 1.42; color: #d7dad3; }
  .skills-heading {
    margin-top: 12px;
    font-weight: 800;
    font-size: 15.5px;
    line-height: 1.35;
  }
  .skills-list {
    margin-top: 8px;
    font-size: 13.5px;
    line-height: 1.45;
    color: #d7dad3;
  }
  .photo {
    position: absolute;
    left: 600px; top: 0;
    width: 440px; height: 600px;
    background: linear-gradient(160deg, var(--photo-light) 0%, #a8aaa3 45%, var(--photo-dark) 100%);
  }
  .brand-box {
    position: absolute;
    left: 620px; top: 44px;
    width: 200px; height: 130px;
    background: var(--paper);
    border: 8px solid var(--slate);
    display: flex; align-items: center; justify-content: center; flex-direction: column;
    gap: 10px;
  }
  .brand-mark { width: 14px; height: 14px; background: var(--slate); }
  .brand-name {
    font-weight: 700;
    font-size: 15px;
    letter-spacing: 2px;
    text-align: center;
    line-height: 1.3;
    color: var(--slate);
    text-transform: uppercase;
  }
  .age-badge {
    position: absolute;
    left: 640px; top: 480px;
    width: 250px; height: 160px;
  }
  .age-badge svg { position: absolute; inset: 0; }
  .age-text {
    position: absolute; inset: 0;
    display: flex; flex-direction: column; align-items: center; justify-content: center;
    font-family: "Oswald", "Arial Narrow", sans-serif;
    color: var(--sage-dark);
    text-transform: uppercase;
    text-align: center;
    line-height: 1.1;
  }
  .age-small { font-size: 19px; font-weight: 400; }
  .age-big { font-size: 32px; font-weight: 500; line-height: 1.15; }
  .recommend {
    position: absolute;
    left: 40px; top: 622px;
    width: 600px;
    font-weight: 800;
    font-size: 22px;
    line-height: 1.35;
    color: var(--ink-green);
  }
</style>
</head>
<body>
  <div class="flyer">
    <section class="info-panel">
      <div class="intro">
        <p class="intro-lead">Pomme Sauvage Riding School, Horses and ponies are carefully matched to suit each rider’s experience, ability and confidence. I am a Qualified instructor, equipped to train all levels from nervous beginners to the more advanced.</p>
        <p class="intro-body">Horse riding is fun! Riders, particularly children, are taught not only skills on the horse, but skills that are integral to good horsemanship and ownership of horses.</p>
      </div>
      <div class="events-band">
        <p class="events-text">We regularly host Ladies Days, Guest Instructors, 1 hour Trail Rides and Pony Ride Days!</p>
      </div>
      <div class="teaching">
        <p class="teaching-lead">We teach people how to interact safely with, and care for horses so they develop a genuine love and respect for the animals and the sport.</p>
        <p class="skills-heading">In addition to fundamental riding techniques including walk, trot, and canter, we teach our students:</p>
        <p class="skills-list">Grooming and Care of horses, Safety around horses, Balance and Co-Ordination, How to saddle up and care for Tack, Responsibility for equipment and horse, Confidence and Confidence Building for all Ages.</p>
      </div>
    </section>

    <div class="photo" role="img" aria-label="Black and white photo of a young child in a riding helmet sitting on a dark horse in an outdoor arena"></div>

    <div class="brand-box">
      <span class="brand-mark"></span>
      <span class="brand-name">Pomme Sauvage<br>Riding School</span>
    </div>

    <div class="age-badge">
      <svg viewBox="0 0 250 160" width="250" height="160" aria-hidden="true">
        <rect x="4" y="4" width="242" height="152" rx="34" fill="#b8bdb2"/>
        <rect x="14" y="14" width="222" height="132" rx="26" fill="#ffffff"/>
      </svg>
      <div class="age-text">
        <span class="age-small">Private and group</span>
        <span class="age-small">lessons start at</span>
        <span class="age-big">5 years of age</span>
        <span class="age-small">upwards</span>
      </div>
    </div>

    <p class="recommend">We recommend children 4 years and under partake in 15 minute pony rides, mainly due to their attention span!</p>
  </div>
</body>
</html>
```